Torvela Lighting needs a new website (only informative)

Torvela Lighting (Pty) Ltd imports and distributes LED lighting products to South Africa. Our existing website (www.torvela.co.za) is designed and implemented on a shopping cart template: Pix-Basket.

The website needs to be redesigned. It should no longer be based on a shopping cart template, but purely informative and allow some PDF downloads. It should scale well and allow quick & easy changes by the website owner: Including adding, changing and removing products. Other information pages should also be easy to manage.

No need to design a logo. A logo and user requirement specification is uploaded with more details.

Target Market(s)

Retailers, interior designers, architects, contractors, electricians, franchises etc. with a need for energy efficient LED lighting.

Industry/Entity Type

Shopping

Font styles to use
Sans Serif

Colors
0355a3
0892cd
86cae6
86cfc6

Requirements
Must have
• Existing logo to be used.
All pages informative & PDF download capability.
User friendly management
SEO capability

```html
<!DOCTYPE html>
<html lang="en">
<head>
<meta charset="utf-8">
<title>Torvela Lighting</title>
<link href="https://fonts.googleapis.com/css2?family=PT+Sans:wght@400;700&display=swap" rel="stylesheet">
<style>
:root{
  --navy:#0d4a6b;
  --blue:#0355a3;
  --bright:#0892cd;
  --sky:#86cae6;
  --text:#333;
  --muted:#666;
  --red:#c0242b;
  --footer:#2e2e2e;
}
*{margin:0;padding:0;box-sizing:border-box}
html,body{width:863px;height:1200px;overflow:hidden}
body{position:relative;font-family:"PT Sans",sans-serif;color:var(--text);background:#f4f5f6}
.abs{position:absolute}
.header{left:0;top:0;width:863px;height:75px;background:#f2f2f2}
.header-inner{left:74px;top:0;width:716px;height:75px;background:#fff;box-shadow:0 0 8px rgba(0,0,0,.12)}
.brand{left:106px;top:18px;font-weight:700;font-size:34px;line-height:40px;color:var(--navy);letter-spacing:1px}
.brand-sub{left:150px;top:54px;font-weight:700;font-size:12px;color:var(--navy);letter-spacing:3px}
.email{left:664px;top:26px;font-size:11px;color:var(--blue);display:flex;align-items:center;gap:7px}
.nav{left:0;top:75px;width:863px;height:41px;background:linear-gradient(#1a86cf,#0a5ea8);border-bottom:2px solid #cfe3f1}
.nav a{position:absolute;top:0;height:41px;line-height:41px;color:#fff;font-size:11px;text-decoration:none}
.nav .active{left:70px;width:100px;background:#b9bfc4;text-align:center;color:#f4f4f4}
.nav .sep{position:absolute;top:0;width:1px;height:41px;background:rgba(255,255,255,.35)}
.search{left:650px;top:86px;width:120px;height:16px;background:#fff;border:1px solid #9cc;font-size:8px;color:#aaa;padding:3px 8px;line-height:9px}
.hero{left:0;top:118px;width:863px;height:335px;background:linear-gradient(90deg,#e6e8ea,#f8f8f8 50%,#eceef0)}
.tagline{left:0;top:258px}
.tagline-text{left:38px;top:282px;color:#fff;font-size:15px;font-variant:small-caps;font-weight:700;line-height:21px;letter-spacing:.3px}
.next{left:790px;top:262px}
.band{left:0;top:453px;width:863px;height:229px;background:var(--sky)}
.card{top:488px;width:180px;height:162px;background:#fff;box-shadow:0 2px 3px rgba(0,0,0,.2)}
.card .pic{position:absolute;left:7px;top:9px;width:166px;height:71px;border:2px solid #c9c9c9;border-radius:3px}
.card h3{position:absolute;left:8px;top:85px;font-size:13px;font-weight:400;font-variant:small-caps;color:var(--blue)}
.card p{position:absolute;left:8px;top:105px;width:162px;font-size:7.3px;line-height:10px;color:var(--muted);text-align:justify}
.card .more{position:absolute;right:13px;top:141px;font-size:8.5px;color:var(--red)}
.welcome{left:119px;top:701px;font-size:19px;color:#1b1b1b;font-weight:400}
.welcome span,.products-title span{color:var(--bright)}
.rule{left:119px;width:401px;height:1px;background:var(--sky)}
.sub{left:120px;top:737px;font-size:12px;color:#444}
.para{left:122px;width:397px;font-size:8.3px;line-height:13px;text-align:justify;color:#333}
.more-link{left:485px;top:877px;font-size:9px;color:var(--red)}
.products-title{left:119px;top:904px;font-size:19px;color:#1b1b1b;font-weight:400}
.thumb{top:952px;width:96px;height:87px;border:2px solid #bbb;border-radius:3px}
.thumb-label{top:1046px;font-size:10.5px;color:#333}
.side{left:562px;width:169px;background:var(--sky);box-shadow:0 3px 2px rgba(0,0,0,.15)}
.side h4{position:absolute;left:3px;top:3px;width:163px;height:27px;background:#fff;border-radius:14px;font-weight:400;font-variant:small-caps;font-size:14px;color:#222;padding:4px 0 0 28px}
.side ul{position:absolute;left:13px;list-style:none}
.side li{font-size:9px;color:#fff;height:17.3px}
.side li::before{content:"›";margin-right:8px;color:#2a5c7a}
.footer{left:0;top:1088px;width:863px;height:112px;background:var(--footer);border-top:3px solid #1c1c1c}
.download{left:114px;top:1108px;width:173px;height:67px;background:var(--bright);border:2px solid #9fd4ee;border-radius:3px}
.download .pdf{position:absolute;left:13px;top:16px;width:32px;height:32px;background:var(--red);border-radius:3px}
.download .t1{position:absolute;left:57px;top:13px;color:#fff;font-size:14px}
.download .t2{position:absolute;left:57px;top:32px;color:#ffe13b;font-size:13px}
.social{top:1110px;width:15px;height:15px;border-radius:2px}
.foot-links{right:138px;top:1144px;font-size:9px;color:#e6e6e6;text-align:right;line-height:18px}
</style>
</head>
<body>
<div class="abs header"></div>
<div class="abs header-inner"></div>
<div class="abs brand">Torvela</div>
<div class="abs brand-sub">LED LIGHTS</div>
<div class="abs email">
  <svg width="12" height="9" viewBox="0 0 12 9"><rect x=".5" y=".5" width="11" height="8" fill="#888"/><path d="M.5 .5 6 5l5.5-4.5" stroke="#fff" fill="none"/></svg>
  info@torvela.co.za
</div>

<nav class="abs nav">
  <a class="active">Company Profile</a>
  <a style="left:184px">Lighting Fundamentals</a>
  <span class="sep" style="left:301px"></span>
  <a style="left:317px">Products</a>
  <span class="sep" style="left:370px"></span>
  <a style="left:385px">Contact</a>
  <span class="sep" style="left:433px"></span>
  <a style="left:449px">References</a>
</nav>
<div class="abs search">Search</div>

<section class="abs hero" role="img" aria-label="Photograph of three round LED downlights"></section>
<svg class="abs tagline" width="352" height="98"><polygon points="0,0 350,0 316,98 0,98" fill="#7f8aa6" opacity=".85"/></svg>
<div class="abs tagline-text">We believe in a cleaner tomorrow.<br>Join us in conserving power.</div>
<svg class="abs next" width="34" height="34" viewBox="0 0 34 34"><circle cx="17" cy="17" r="15.5" fill="#1474c4" stroke="#cfe6f6" stroke-width="2"/><path d="M14 10l7 7-7 7" stroke="#fff" stroke-width="3" fill="none"/></svg>

<div class="abs band"></div>
<div class="abs card" style="left:118px"><div class="pic" style="background:#c4c8c3" role="img" aria-label="Photograph of a multi-LED downlight fitting"></div><h3>LED Products</h3><p>Sed ut perspiciatis unde omnis iste natus error voluptatem accusantium doloremque laudantium, totam aperiam, eaque ipsa quae.</p><span class="more">Read More &gt;&gt;</span></div>
<div class="abs card" style="left:334px"><div class="pic" style="background:#5a6c9e" role="img" aria-label="Photograph of solar panels"></div><h3>Solar Products</h3><p>Sed ut perspiciatis unde omnis iste natus error voluptatem accusantium doloremque laudantium, totam aperiam, eaque ipsa quae.</p><span class="more">Read More &gt;&gt;</span></div>
<div class="abs card" style="left:551px"><div class="pic" style="background:#d8ccA4" role="img" aria-label="Photograph of an LED bulb"></div><h3>Smart Grid Solutions</h3><p>Sed ut perspiciatis unde omnis iste natus error voluptatem accusantium doloremque laudantium, totam aperiam, eaque ipsa quae.</p><span class="more">Read More &gt;&gt;</span></div>

<h1 class="abs welcome">Welcome to <span>Torvela</span></h1>
<div class="abs rule" style="top:730px"></div>
<div class="abs sub">Mauris Vitae Felis Vestibulum Volutpat.</div>
<p class="abs para" style="top:763px">Sed ut perspiciatis unde omnis iste natus error sit voluptatem accusantium doloremque laudantium, totam rem aperiam, eaque ipsa quae ab illo inventore veritatis et quasi architecto beatae vitae dicta sunt explicabo.Sed ut perspiciatis unde omnis iste natus error sit voluptatem accusantium doloremque laudantium, totam rem aperiam, eaque ipsa quae ab illo inventore veritatis et quasi architecto beatae vitae dicta sunt explicabo.</p>
<p class="abs para" style="top:840px">Sed ut perspiciatis unde omnis iste natus error sit voluptatem accusantium doloremque laudantium, totam rem aperiam, eaque ipsa quae ab illo inventore veritatis et quasi architecto beatae vitae dicta sunt explicabo.</p>
<span class="abs more-link">More &nbsp;&gt;&gt;</span>

<h2 class="abs products-title">Our <span>Products</span></h2>
<div class="abs rule" style="top:933px"></div>
<div class="abs thumb" style="left:118px;background:#1f4a3c" role="img" aria-label="Photograph of a downlight"></div>
<div class="abs thumb" style="left:221px;background:#2d6fb5" role="img" aria-label="Photograph of a compact bulb"></div>
<div class="abs thumb" style="left:325px;background:#2a3384" role="img" aria-label="Photograph of LED tubes"></div>
<div class="abs thumb" style="left:429px;background:#7d88a6" role="img" aria-label="Photograph of solar panels"></div>
<span class="abs thumb-label" style="left:120px">Downlights</span>
<span class="abs thumb-label" style="left:223px">Bulbs</span>
<span class="abs thumb-label" style="left:327px">Tubes</span>
<span class="abs thumb-label" style="left:431px">Panels</span>

<aside class="abs side" style="top:709px;height:135px">
  <h4>Important Links</h4>
  <ul style="top:40px"><li>Gridwise Rebate</li><li>LED Advantages</li><li>Luminous power &amp; efficiency</li><li>Light Colour Temperature</li><li>Torvela Wholesale</li></ul>
</aside>
<aside class="abs side" style="top:875px;height:171px">
  <h4>Categories</h4>
  <ul style="top:42px"><li>LED down lights (9)</li><li>LED bulbs (4)</li><li>LED tube lights (2)</li><li>Dimmable LED lamps (5)</li><li>Flood Lights (4)</li><li>LED strip lights</li><li>Other LED lights (2)</li></ul>
</aside>

<footer class="abs footer"></footer>
<div class="abs download"><div class="pdf"></div><span class="t1">Benefits Of LED</span><span class="t2">Download</span></div>
<div class="abs social" style="left:595px;background:#3b5a99"></div>
<div class="abs social" style="left:624px;background:#3fa9e0"></div>
<div class="abs social" style="left:653px;background:#f07a22"></div>
<div class="abs social" style="left:682px;background:#1f78b4"></div>
<div class="abs social" style="left:711px;background:#444"></div>
<div class="abs foot-links">Blog &nbsp;|&nbsp; Terms &nbsp;|&nbsp; Privacy Policy &nbsp;|&nbsp; Sitemap<br>© 2013 torvela.com, All Rights Reserved</div>
</body>
</html>
```